Derek Hollins Business card

Hey there, I’m hoping to have a business card designed. I’m in Real estate and just switched to a new Brokerage called: The Property Quarter

The back could just be the company name maybe or whatever looks good!

I’ve attached some logos of our company and some cards my buddy had done up.

On the card:
Derek Hollins
derekhollins@mailbox-demo.com
587-214-6093
derekhollins-demo.ca

Target Market(s)

Home buyers and sellers

Industry/Entity Type

Real Estate

Contact Information for Business Card

just looking for a cool and modern design with my picture on it. I like the idea of Black and red being used.

Requirements
Must have
• all the details provided. I'm open to anything. Just want a professional looking card.

```html
<!DOCTYPE html>
<html lang="en">
<head>
<meta charset="utf-8">
<title>Derek Hollins — Business Card</title>
<link href="https://fonts.googleapis.com/css2?family=Montserrat:wght@400;500;700;800&display=swap" rel="stylesheet">
<style>
  :root {
    --canvas-bg: #969696;
    --card-bg: #222126;
    --brand-red: #d0203f;
    --text-light: #ffffff;
    --emboss: #2e2d33;
  }
  html, body {
    margin: 0;
    padding: 0;
    width: 1200px;
    height: 1000px;
    overflow: hidden;
    background: var(--canvas-bg);
    font-family: "Montserrat", Arial, sans-serif;
  }
  .canvas {
    position: relative;
    width: 1200px;
    height: 1000px;
  }
  .card {
    position: absolute;
    left: 293px;
    width: 615px;
    height: 354px;
    border-radius: 18px;
    background: var(--card-bg);
    overflow: hidden;
  }
  .card--front { top: 90px; }
  .card--back { top: 526px; }

  .front-mark {
    position: absolute;
    inset: 0;
    display: flex;
    align-items: center;
    justify-content: center;
    color: var(--emboss);
    font-weight: 800;
    font-size: 38px;
    letter-spacing: 1px;
    text-transform: uppercase;
    text-align: center;
    line-height: 1.05;
  }

  .identity {
    position: absolute;
    left: 18px;
    top: 58px;
    width: 300px;
    text-align: center;
    color: var(--text-light);
  }
  .brand-name {
    font-weight: 800;
    font-size: 24px;
    line-height: 1.05;
    text-transform: uppercase;
    letter-spacing: 0.5px;
    color: var(--text-light);
    margin: 0;
  }
  .agent-name {
    margin: 64px 0 0;
    font-size: 26px;
    font-weight: 400;
    letter-spacing: 0.8px;
    line-height: 26px;
    white-space: nowrap;
  }
  .agent-name .surname {
    font-weight: 700;
    color: var(--brand-red);
  }
  .contact-icons {
    display: flex;
    justify-content: center;
    gap: 4px;
    margin-top: 10px;
  }
  .contact-icons svg { display: block; }
  .contact-list {
    list-style: none;
    margin: 9px 0 0;
    padding: 0;
    font-size: 15px;
    font-weight: 500;
    letter-spacing: 0.3px;
    line-height: 19px;
    white-space: nowrap;
  }
  .portrait {
    position: absolute;
    left: 312px;
    top: 0;
    width: 303px;
    height: 354px;
    background: linear-gradient(160deg, #3a3a3f 0%, #2a2d33 55%, #1d2026 100%);
  }
</style>
</head>
<body>
<div class="canvas">
  <section class="card card--front" aria-label="Card front">
    <div class="front-mark">The Property<br>Quarter</div>
  </section>

  <section class="card card--back" aria-label="Card back">
    <div class="identity">
      <p class="brand-name">The Property<br>Quarter</p>
      <h1 class="agent-name">DEREK <span class="surname">HOLLINS</span></h1>
      <div class="contact-icons" aria-hidden="true">
        <svg width="24" height="24" viewBox="0 0 24 24">
          <circle cx="12" cy="12" r="12" fill="var(--brand-red)"/>
          <path d="M8.6 6.8c.4-.3 1-.2 1.2.2l1 1.8c.2.4.1.8-.2 1.1l-.7.6c.5 1.2 1.4 2.1 2.6 2.7l.6-.7c.3-.3.8-.4 1.1-.2l1.8 1c.4.2.5.8.2 1.2l-.8 1c-.4.5-1.1.7-1.7.5-3-1-5.3-3.3-6.3-6.3-.2-.6 0-1.3.5-1.7z" fill="#fff"/>
        </svg>
        <svg width="24" height="24" viewBox="0 0 24 24">
          <circle cx="12" cy="12" r="12" fill="var(--brand-red)"/>
          <rect x="6.5" y="8" width="11" height="8" rx="1" fill="#fff"/>
          <path d="M6.8 8.4 12 12.3l5.2-3.9" fill="none" stroke="var(--brand-red)" stroke-width="1.2"/>
        </svg>
        <svg width="24" height="24" viewBox="0 0 24 24">
          <circle cx="12" cy="12" r="12" fill="var(--brand-red)"/>
          <g fill="none" stroke="#fff" stroke-width="1.2">
            <circle cx="12" cy="12" r="5.5"/>
            <ellipse cx="12" cy="12" rx="2.3" ry="5.5"/>
            <path d="M6.5 12h11M7.3 9.3h9.4M7.3 14.7h9.4"/>
          </g>
        </svg>
      </div>
      <ul class="contact-list">
        <li>587-214-6093</li>
        <li>derekhollins@mailbox-demo.com</li>
        <li>derekhollins-demo.ca</li>
      </ul>
    </div>
    <div class="portrait" role="img" aria-label="Portrait photo of Derek Hollins in a dark suit and white shirt"></div>
  </section>
</div>
</body>
</html>
```